Package of web graphics needed

Utilizing a recently selected logo from a Pixel Harbor contest, we need to have some ads, fb cover, home page slide image created for our new 844-Toll-Free Number Product. Please feel free to check our site at www.ringvantagehub.com

You'll find attached the 844 toll free logo in 2 layouts.

Here are the ads and dimensions of each that are needed:
1.)Banners/ads - 468x60
468×60 px
125×125 px
120×600 px
120x90 px
88×31 px button
5.)FB Cover - 851 x 315
6.)Home page slider image - 944 x 328

Here is the text & some ideas to use for these. Feel free to use different versions depending on which ad they work better on:
-

Market Your Business in a Memorable Way – Pre-Order Yours Today, Deadline: Dec. 7th
[include logo]
-
[844 logo] Don't Miss out on your chance to finally get a great vanity!

Order Yours Today
-

Don't Miss out on your chance to finally get a great vanity!
Dec. 7th Deadline to pre-order

Don't Ignore 844!– The newest toll free prefix – Coming Dec. 7th – Get Yours Today

FB COVER guidelines -
Requirements:
Include the logo
Limited Time Left – Get your Reservation in by December 7th

HOME PAGE Image Slide:
Use the logo,

Couple of Ideas we're interested in seeing:

[Billboard sign stock image … with the number 877-Grab-ONE on the billboard]
[844 logo and caricature] [1 caricature looking surprised]

```html
<!DOCTYPE html>
<html lang="en">
<head>
<meta charset="utf-8">
<title>RingVantage Lines – Cover</title>
<link href="https://fonts.googleapis.com/css2?family=Roboto:wght@300;400;700&display=swap" rel="stylesheet">
<style>
  :root {
    --bg-centre: #ffc61a;
    --bg-edge: #f29200;
    --ink: #111111;
    --brand-navy: #17386f;
    --hair: #d9641f;
    --skin: #f4c9a3;
    --shirt: #e9728f;
  }
  html, body {
    margin: 0;
    padding: 0;
    overflow: hidden;
  }
  .cover {
    position: relative;
    width: 1200px;
    height: 444px;
    overflow: hidden;
    background: radial-gradient(ellipse 70% 90% at 48% 45%, var(--bg-centre) 0%, #f8b000 55%, var(--bg-edge) 100%);
    font-family: "Roboto", Arial, sans-serif;
    color: var(--ink);
  }
  .portrait {
    position: absolute;
    top: 0;
    right: 0;
    width: 490px;
    height: 444px;
    background:
      radial-gradient(ellipse 34% 40% at 70% 46%, var(--skin) 0%, rgba(244, 201, 163, 0.6) 60%, rgba(244, 201, 163, 0) 100%),
      radial-gradient(ellipse 45% 20% at 78% 100%, var(--shirt) 0%, rgba(233, 114, 143, 0) 100%),
      linear-gradient(to right, rgba(217, 100, 31, 0) 0%, rgba(217, 100, 31, 0.35) 30%, rgba(217, 100, 31, 0.55) 100%);
  }
  .headline {
    position: absolute;
    top: 58px;
    left: 190px;
    width: 800px;
    margin: 0;
    text-align: center;
    font-weight: 400;
    font-size: 43px;
    line-height: 50px;
    letter-spacing: 0.2px;
  }
  .brand {
    position: absolute;
    top: 236px;
    left: 380px;
    width: 400px;
    display: flex;
    align-items: center;
    justify-content: center;
    gap: 14px;
    color: var(--brand-navy);
    font-weight: 700;
    font-size: 38px;
  }
  .brand-mark {
    width: 34px;
    height: 34px;
    background: var(--brand-navy);
    border-radius: 4px;
  }
  .deadline {
    position: absolute;
    top: 372px;
    left: 380px;
    width: 400px;
    margin: 0;
    text-align: center;
    font-weight: 300;
    font-size: 18.5px;
    line-height: 21px;
  }
</style>
</head>
<body>
  <div class="cover">
    <div class="portrait" role="img" aria-label="Photo of a surprised red-haired child with a braid flying sideways"></div>
    <h1 class="headline">Don’t Miss out on your chance<br>to finally get a great vanity!</h1>
    <div class="brand"><span class="brand-mark"></span><span class="brand-name">RingVantage Lines</span></div>
    <p class="deadline">Limited Time Left!<br>Get your Reservation in by December 7th</p>
  </div>
</body>
</html>
```